Business Card Design Falcon Ridge Autos

Used car dealership, We buy, sell, trade and finance a cars.

Industry/Entity Type

Finance

Contact Information for Business Card

Falcon Ridge Autos, Buy, Sell, Trade, Finance, 418 Larkspur Ave, Alderwick, ZZ, 04837, 555-318-6092, www.Falcon-Ridge-Autos.example

Requirements
Must have
• Crown
Nice to have
• purple and gold colors

```html
<!DOCTYPE html>
<html lang="en">
<head>
<meta charset="utf-8">
<title>Falcon Ridge Autos – Business Card</title>
<link rel="stylesheet" href="https://fonts.googleapis.com/css2?family=Playfair+Display:wght@800&family=Open+Sans:wght@400;700&display=swap">
<style>
  :root {
    --backdrop: #7d8791;
    --purple: #6419a3;
    --purple-deep: #2c0a4c;
    --purple-mid: #4a1480;
    --gold: #f0c419;
    --white: #ffffff;
  }
  * { box-sizing: border-box; margin: 0; padding: 0; }
  html, body { width: 1200px; height: 1024px; overflow: hidden; }
  body {
    background: var(--backdrop);
    font-family: "Open Sans", Arial, sans-serif;
    position: relative;
  }
  .card {
    position: absolute;
    left: 215px;
    width: 770px;
    height: 440px;
    overflow: hidden;
    box-shadow: 0 10px 24px rgba(0,0,0,.35);
    background: var(--purple);
  }
  .card--front { top: 48px; }
  .card--back { top: 536px; }
  .card__photo {
    position: absolute; inset: 0;
    background:
      radial-gradient(ellipse at 55% 40%, rgba(120,50,190,.55), transparent 60%),
      linear-gradient(160deg, var(--purple) 0%, var(--purple-mid) 55%, var(--purple-deep) 100%);
  }
  .card--back .card__photo {
    background:
      radial-gradient(ellipse at 40% 35%, rgba(110,40,180,.5), transparent 60%),
      linear-gradient(200deg, var(--purple) 10%, var(--purple-mid) 55%, var(--purple-deep) 100%);
  }
  .brand-name {
    font-family: "Playfair Display", Georgia, serif;
    font-weight: 800;
    color: var(--white);
    text-transform: uppercase;
    letter-spacing: -1px;
    line-height: 1;
    display: flex;
    align-items: center;
    gap: 12px;
    white-space: nowrap;
  }
  .brand-name__dot {
    width: 14px; height: 14px; border-radius: 50%;
    background: var(--gold); flex: none;
  }
  .front-lockup {
    position: absolute; inset: 0;
    display: flex; flex-direction: column;
    align-items: center; justify-content: center;
  }
  .front-lockup .brand-name { font-size: 46px; }
  .tagline {
    margin-top: 14px;
    color: var(--white);
    font-size: 20px;
    letter-spacing: .5px;
  }
  .tagline .sep { color: var(--gold); margin: 0 10px; }
  .front-web {
    margin-top: 40px;
    color: var(--gold);
    font-size: 19px;
  }
  .back-content {
    position: absolute; top: 48px; right: 0; bottom: 40px;
    display: flex; flex-direction: column; align-items: flex-end;
    text-align: right;
  }
  .back-content .brand-name { font-size: 34px; margin-right: 48px; }
  .person {
    margin-top: 40px;
    display: flex; align-items: stretch; gap: 20px;
  }
  .person__name { color: var(--gold); font-weight: 700; font-size: 24px; line-height: 1.2; }
  .person__role { color: var(--white); font-size: 17px; }
  .person__bar { width: 28px; background: var(--gold); }
  .contact {
    margin-top: 22px; margin-right: 48px;
    color: var(--white); font-size: 17px; line-height: 1.55;
    list-style: none;
  }
  .contact li { display: flex; align-items: center; justify-content: flex-end; gap: 10px; }
  .contact svg { width: 15px; height: 15px; fill: var(--gold); flex: none; }
</style>
</head>
<body>

<section class="card card--front">
  <div class="card__photo" role="img" aria-label="Dim purple-toned photograph of a car front"></div>
  <div class="front-lockup">
    <div class="brand-name"><span class="brand-name__dot"></span>Falcon Ridge Autos Inc.</div>
    <p class="tagline">Buy<span class="sep">•</span>Sell<span class="sep">•</span>Trade<span class="sep">•</span>Finance</p>
    <p class="front-web">www.Falcon-Ridge-Autos.example</p>
  </div>
</section>

<section class="card card--back">
  <div class="card__photo" role="img" aria-label="Dim purple-toned photograph of a car front"></div>
  <div class="back-content">
    <div class="brand-name"><span class="brand-name__dot"></span>Falcon Ridge Autos Inc.</div>
    <div class="person">
      <div>
        <p class="person__name">Dana Whitaker</p>
        <p class="person__role">Owner</p>
      </div>
      <span class="person__bar"></span>
    </div>
    <ul class="contact">
      <li>418 Larkspur Ave</li>
      <li>Alderwick, ZZ 04837</li>
      <li>555-318-6092
        <svg viewBox="0 0 24 24" aria-hidden="true"><path d="M6.6 10.8a15.1 15.1 0 0 0 6.6 6.6l2.2-2.2c.3-.3.7-.4 1-.2 1.1.4 2.3.6 3.6.6.6 0 1 .4 1 1V20c0 .6-.4 1-1 1A17 17 0 0 1 3 4c0-.6.4-1 1-1h3.5c.6 0 1 .4 1 1 0 1.3.2 2.5.6 3.6.1.3 0 .7-.2 1z"/></svg>
      </li>
      <li>www.Falcon-Ridge-Autos.example
        <svg viewBox="0 0 24 24" aria-hidden="true"><path d="M12 2a10 10 0 1 0 0 20 10 10 0 0 0 0-20zm6.9 6h-3a15.6 15.6 0 0 0-1.4-3.6A8 8 0 0 1 18.9 8zM12 4c.8 1.2 1.5 2.5 1.9 4h-3.8c.4-1.5 1.1-2.8 1.9-4zM4.3 14a8.2 8.2 0 0 1 0-4h3.4a16.5 16.5 0 0 0 0 4zm.8 2h3a15.6 15.6 0 0 0 1.4 3.6A8 8 0 0 1 5.1 16zm3-8h-3a8 8 0 0 1 4.4-3.6C8.9 5.5 8.4 6.7 8.1 8zM12 20c-.8-1.2-1.5-2.5-1.9-4h3.8c-.4 1.5-1.1 2.8-1.9 4zm2.3-6H9.7a14.7 14.7 0 0 1 0-4h4.6a14.7 14.7 0 0 1 0 4zm.3 5.6c.6-1.1 1.1-2.3 1.4-3.6h3a8 8 0 0 1-4.4 3.6zm1.7-5.6a16.5 16.5 0 0 0 0-4h3.4a8.2 8.2 0 0 1 0 4z"/></svg>
      </li>
    </ul>
  </div>
</section>

</body>
</html>
```